Powerpoint Design for business and consulting company - Brennig-Tautz

I am searching a design specialist who can help me to create a PowerPoint Design for my company. I'm in the business coaching and consulting industry.

The PPT master should be easy to use and include professional formatting (using the fonts of my website). In general, the slide master should have the look and feel of my website (in terms of fonts, colors, logos, possibility to place big photographs, having text and graph slides as well as photo slides with just 1 key message).

The PowerPoint design should fit my cooperate Identity (please see my website https://brennig-tautz.de).
My logos are attached.

Additional information:
- wide screen format - 16: 9
- right set up of a fitting color scheme
https: // tintrow. io / f6ded1-bfcbce-807f84-9cd3d1-666666
# 666666 (Dim Gray) - body / heading text
# 807F84 (Gray Web)
#BFCBCE (Silver Sand) - link hover
# 9cd3d1 (Powder Blue) - Link color
# F6DED1 (Champagne Pink)

- creation of chart templates, using chart tools, and different chart types etc.
- creation of different slide layouts to place content, pictures (in different sizes), optionally Media
- set up of display guide lines
- as well as standard elements, such as text boxes, lines, default shapes, etc.

• Powerpoint Design needs to have:
https://tintrow.io/f6ded1-bfcbce-807f84-9cd3d1-666666
# 807F84 (Gray Web)
# F6DED1 (Champagne Pink)

```html
<!DOCTYPE html>
<html lang="en">
<head>
<meta charset="utf-8">
<title>Brennig-Tautz – Presentation Master</title>
<link href="https://fonts.googleapis.com/css2?family=Lato:wght@300;400;700;900&display=swap" rel="stylesheet">
<style>
:root{
  --teal:#9cd3d1;--teal-dark:#86c4c2;--pink:#f6ded1;--silver:#bfcbce;
  --gray:#807f84;--dim:#666666;--white:#ffffff;--paper:#f4f6f6;--frame:#9aa3a6;
}
*{box-sizing:border-box;margin:0;padding:0}
html,body{width:1200px;height:2501px;overflow:hidden;background:var(--frame)}
body{font-family:'Lato',sans-serif;color:var(--dim)}
.deck{width:1200px;height:2501px;padding:3px;display:grid;grid-template-columns:repeat(3,1fr);grid-template-rows:repeat(11,1fr);gap:5px}
.slide{position:relative;overflow:hidden;background:var(--white)}
.abs{position:absolute}
.fill{position:absolute;inset:0}
svg.fill{width:100%;height:100%}
.lorem{font-size:4.4px;line-height:1.5;color:var(--gray)}
.lorem.white{color:var(--white)}
.logo{position:absolute;display:flex;align-items:center;gap:4px;font-weight:700;font-size:9px;color:var(--dim);white-space:nowrap}
.logo i{display:block;width:7px;height:7px;border-radius:50%;background:currentColor}
.logo.big{font-size:13px}
.logo.light{color:var(--white)}
.foot{left:8px;bottom:5px;font-size:7px}
.foot i{width:5px;height:5px}
.pg{position:absolute;right:12px;bottom:7px;font-size:3.6px;letter-spacing:.8px;color:var(--gray)}
.accent{position:absolute;left:17px;top:14px;width:1px;height:20px;background:var(--pink)}
.cover-title{position:absolute;color:var(--white);font-weight:300;font-size:16px;line-height:1.25;border-left:1.5px solid var(--pink);padding-left:10px}
.photo-office{background:linear-gradient(135deg,#5b4a3d 0%,#8a6e58 35%,#3e4750 60%,#6d5a4a 100%)}
.photo-stairs{background:linear-gradient(120deg,#8c8c86 0%,#c9c7c0 40%,#d9826a 55%,#a9a8a2 75%,#777a78 100%)}
.photo-lightbox{background:radial-gradient(ellipse at 60% 40%,#f0efe9 0%,#cfcdc7 30%,#2f3a40 65%,#1c2428 100%)}
.photo-valley{background:linear-gradient(180deg,#9fb6cc 0%,#d9e2ea 35%,#8c9b7d 60%,#4d5d3a 100%)}
.photo-forest{background:linear-gradient(160deg,#1f3a2c 0%,#3f5e44 40%,#6d5a4a 70%,#2b3b2e 100%)}
.photo-portrait{background:linear-gradient(160deg,#d8d8d8 0%,#9a9a9a 55%,#5e5e5e 100%)}
.photo-waterfall{background:linear-gradient(180deg,#2d4a3c 0%,#8fa9a3 45%,#2e4a3b 100%)}
.photo-tower{background:linear-gradient(100deg,#8f9699 0%,#d2d7d9 50%,#9aa1a4 100%)}
.photo-city{background:linear-gradient(120deg,#5c5650 0%,#c9b08a 45%,#f2c27a 60%,#3d3a37 100%)}
.photo-notes{background:linear-gradient(140deg,#e7e4df 0%,#f6d9a4 40%,#f2b6b4 60%,#e9e6e2 100%)}
.photo-meeting{background:linear-gradient(160deg,#a4a4a4 0%,#5a5a5a 50%,#cfcfcf 100%)}
.photo-compass{background:linear-gradient(160deg,#9cb3c7 0%,#7a8f55 60%,#5a6b3c 100%)}
.photo-laptop{background:linear-gradient(160deg,#e9dfd6 0%,#b9a998 60%,#8c7e70 100%)}
.photo-team{background:linear-gradient(160deg,#d7cdbf 0%,#a88e74 55%,#efe8df 100%)}
.round{border-radius:6px}
.qcircle{position:absolute;width:15px;height:15px;border-radius:50%;background:var(--teal);color:var(--white);font-size:10px;font-weight:900;text-align:center;line-height:17px}
/* agenda */
.agenda-list{position:absolute;left:136px;top:58px;width:210px;list-style:none}
.agenda-list li{display:flex;font-size:6.4px;height:15.5px;align-items:center}
.agenda-list b{width:22px;font-weight:400;color:var(--white);text-align:right;padding-right:6px}
.agenda-list span{flex:1;border-bottom:.5px solid var(--silver);height:100%;display:flex;align-items:center;padding-left:4px;color:var(--dim)}
.h-sm{font-size:7px;font-weight:700;color:var(--dim)}
.h-teal{font-size:5px;font-weight:700;color:var(--teal)}
.dot{display:inline-block;width:6px;height:6px;border-radius:50%;border:.8px solid var(--pink);flex:none}
.row{display:flex;gap:5px;align-items:flex-start}
.num{width:10px;height:10px;border-radius:50%;background:var(--teal);color:var(--white);font-size:4px;text-align:center;line-height:10px;flex:none}
.icon-c{width:18px;height:18px;border-radius:50%;background:var(--silver);flex:none;border:2px solid #e4eaeb}
.card-sh{background:var(--white);box-shadow:0 1px 4px rgba(0,0,0,.15)}
.tbl{position:absolute;left:37px;top:18px;width:328px;border-collapse:collapse;font-size:4px}
.tbl th{background:var(--teal-dark);color:var(--white);text-align:left;padding:5px 4px;font-size:5px;font-weight:700;border-right:1px solid var(--white)}
.tbl td{background:var(--teal);color:var(--white);padding:5px 4px;line-height:1.4;border-right:1px solid var(--white);border-top:1px solid var(--white);vertical-align:top}
.tbl td b{display:block;font-size:4.6px}
.contact-row{display:flex;align-items:center;gap:8px;font-size:4.8px;height:20px}
</style>
</head>
<body>
<main class="deck">

<!-- 1 cover gray -->
<section class="slide" style="background:var(--silver)">
  <div class="fill photo-office" role="img" aria-label="Overhead photo of a desk with laptops, tablet and coffee"></div>
  <div class="abs" style="left:-210px;top:-170px;width:540px;height:540px;border-radius:50%;background:var(--silver)"></div>
  <h1 class="cover-title" style="left:22px;top:85px">Your title goes here<br>One-two sentences</h1>
  <div class="logo light" style="left:28px;top:188px"><i></i>Brennig-Tautz</div>
</section>

<!-- 2 cover white -->
<section class="slide">
  <div class="abs" style="left:-210px;top:-170px;width:540px;height:540px;border-radius:50%;background:var(--silver)"></div>
  <h1 class="cover-title" style="left:22px;top:85px">Your title goes here<br>One-two sentences</h1>
  <div class="logo light" style="left:28px;top:188px"><i></i>Brennig-Tautz</div>
</section>

<!-- 3 cover teal -->
<section class="slide">
  <div class="fill photo-stairs" role="img" aria-label="Photo of a coach in a coral blazer sitting on outdoor steps"></div>
  <div class="abs" style="left:170px;top:-150px;width:600px;height:600px;border-radius:50%;background:var(--teal)"></div>
  <h1 class="cover-title" style="right:18px;top:90px;text-align:right;border:0">Your title goes here<br>One-two sentences</h1>
  <div class="logo light" style="right:18px;top:188px"><i></i>Brennig-Tautz</div>
</section>

<!-- 4 cover photo circle -->
<section class="slide" style="background:var(--teal)">
  <div class="abs photo-lightbox" style="left:-40px;top:-60px;width:340px;height:260px;border-radius:0 0 60% 0" role="img" aria-label="Photo of a lightbox sign reading think outside the box"></div>
  <div class="logo light" style="left:12px;top:188px;font-size:11px"><i></i>Brennig-Tautz</div>
  <div class="abs" style="right:32px;top:189px;color:var(--white);font-size:7.5px;font-weight:700;letter-spacing:1.6px">ADD YOUR TEXT HERE</div>
</section>

<!-- 5 agenda -->
<section class="slide">
  <div class="abs" style="left:0;top:0;width:150px;height:100%;background:var(--teal)"></div>
  <h2 class="abs" style="left:36px;top:104px;color:var(--white);font-size:15px;font-weight:400">AGENDA</h2>
  <ol class="agenda-list">
    <li><b>01</b><span>Introduction - Welcome</span></li>
    <li><b>02</b><span>Mission &amp; Vision</span></li>
    <li><b>03</b><span>Our Services</span></li>
    <li><b>04</b><span>Company Profile</span></li>
    <li><b>05</b><span>Project Portfolio</span></li>
    <li><b>06</b><span>Our Team</span></li>
    <li><b>07</b><span>Our Offices</span></li>
    <li><b>08</b><span>Q&amp;As / Closing Speech</span></li>
  </ol>
  <div class="logo light" style="left:28px;top:196px"><i></i>Brennig-Tautz</div>
  <div class="pg">PAGE | 5</div>
</section>

<!-- 6 quote photo -->
<section class="slide">
  <div class="fill photo-stairs" role="img" aria-label="Photo of a smiling coach sitting on stone steps"></div>
  <div class="fill" style="background:linear-gradient(180deg,rgba(255,255,255,0) 35%,#fff 62%)"></div>
  <div class="qcircle" style="left:190px;top:128px">“</div>
  <p class="lorem abs" style="left:75px;top:150px;width:245px;text-align:center;color:var(--dim)">Lorem ipsum dolor sit amet, consectetur adipiscing elit. Lorem ipsum dolor sit amet, consectetur adipiscing elit, sed do eiusmod tempor incididunt ut labore et dolore magna aliqua.</p>
  <div class="abs" style="left:0;width:100%;top:190px;text-align:center;font-size:5.5px">Your Name</div>
  <div class="logo foot"><i></i>BT</div>
  <div class="pg">PAGE | 6</div>
</section>

<!-- 7 quote landscape -->
<section class="slide">
  <div class="fill photo-valley" role="img" aria-label="Photo of a hiker standing on a rock above a green valley"></div>
  <svg class="fill" viewBox="0 0 395 222" preserveAspectRatio="none"><path d="M0 176 Q200 168 395 150 L395 222 L0 222Z" fill="#9cd3d1"/></svg>
  <div class="abs" style="left:10px;top:188px;width:15px;height:15px;border:1px solid #fff;border-radius:50%;color:#fff;font-size:9px;text-align:center;line-height:16px;font-weight:900">“</div>
  <p class="lorem white abs" style="left:34px;top:184px;width:320px">Lorem ipsum dolor sit amet, consectetur adipiscing elit. Lorem ipsum dolor sit amet, consectetur adipiscing elit, sed do eiusmod tempor incididunt ut labore et dolore magna aliqua.</p>
  <div class="abs" style="left:30px;top:206px;color:#fff;font-size:5.5px">Your Name</div>
</section>

<!-- 8 section divider overlay -->
<section class="slide">
  <div class="fill photo-forest" role="img" aria-label="Photo of a woman on a wooden bridge in a forest"></div>
  <div class="abs" style="left:105px;top:163px;width:165px;height:30px;border-radius:15px 0 0 15px;background:rgba(220,230,232,.45)"></div>
  <div class="abs" style="left:110px;top:168px;width:20px;height:20px;border-radius:50%;background:var(--teal)"></div>
  <div class="abs" style="left:135px;top:165px;color:rgba(255,255,255,.8);font-size:13px;font-weight:300">SECTION DIVIDER</div>
  <div class="abs" style="left:135px;top:182px;color:#fff;font-size:5px;font-weight:700">SECTION SUBTITLE</div>
</section>

<!-- 9 section divider wave -->
<section class="slide">
  <div class="fill photo-forest" role="img" aria-label="Photo of a woman on a wooden bridge in a forest"></div>
  <svg class="fill" viewBox="0 0 395 222" preserveAspectRatio="none"><path d="M0 182 Q220 178 395 150 L395 222 L0 222Z" fill="#9cd3d1"/></svg>
  <div class="abs" style="left:16px;top:187px;color:#fff;font-size:13px;font-weight:700">SECTION DIVIDER</div>
  <div class="abs" style="left:16px;top:203px;color:#fff;font-size:5px">SECTION SUBTITLE</div>
  <div class="logo light" style="right:10px;top:203px;font-size:7px"><i></i>Brennig-Tautz</div>
</section>

<!-- 10 about me -->
<section class="slide">
  <div class="abs" style="left:0;top:0;width:90px;height:100%;background:var(--silver)"></div>
  <div class="abs card-sh" style="left:42px;top:38px;width:88px;height:142px;border-radius:6px;padding:5px">
    <div class="photo-portrait" style="width:100%;height:100%;border-radius:4px" role="img" aria-label="Black and white portrait of the coach"></div>
  </div>
  <h2 class="abs" style="left:152px;top:46px;font-size:14px;font-weight:400">Über Mich</h2>
  <div class="abs lorem" style="left:152px;top:72px;width:190px;text-align:justify">
    <p>Mit Feingefühl, einer wertschätzenden Haltung, Visionskraft und ausgeprägten Kommunikationsfähigkeiten begleite ich seit 22 Berufsjahren Menschen und Organisationen in unterschiedlichsten Experten-, Coach- und Beraterrollen.</p><br>
    <p>Führungskultur entwickeln, Kommunikation für Veränderung gestalten, agiles Arbeiten fördern oder die Digitalisierung vorantreiben – meine Themenfelder sind vielfältig. Dabei habe ich immer mit dem Anspruch verfolgt, Mitarbeiter:innen einzubinden und gut mitzunehmen.</p><br>
    <p>Meine große Leidenschaft ist es deshalb, Menschen und Organisationen im Wandel zu begleiten und ihnen neue Möglichkeitsräume zu eröffnen.</p>
  </div>
  <div class="pg">PAGE | 10</div>
</section>

<!-- 11 program context -->
<section class="slide">
  <div class="abs" style="left:0;top:0;width:130px;height:100%;background:var(--teal)"></div>
  <h2 class="abs" style="left:15px;top:37px;width:110px;color:#fff;font-size:13px;font-weight:700;line-height:1.2">Program context and deliverables slide</h2>
  <p class="lorem white abs" style="left:15px;top:120px;width:95px;text-align:justify">Lorem ipsum dolor sit amet, consectetur adipiscing elit, sed do eiusmod tempor incididunt ut labore et dolore magna aliqua. Ut enim ad minim veniam, quis nostrud exercitation ullamco laboris nisi ut aliquip.</p>
  <div class="abs photo-waterfall" style="left:130px;top:0;width:135px;height:100%" role="img" aria-label="Photo of a person standing before a forest waterfall"></div>
  <div class="abs" style="left:272px;top:44px;width:110px">
    <div class="h-teal">Strategy for online Learning</div>
    <p class="lorem">Lorem ipsum dolor sit amet, consectetur adipiscing elit, sed do eiusmod tempor incididunt ut labore et dolore magna aliqua.</p>
    <div class="h-teal" style="margin-top:18px">Strategy for online Learning</div>
    <p class="lorem">Lorem ipsum dolor sit amet, consectetur adipiscing elit, sed do eiusmod tempor incididunt ut labore et dolore magna aliqua.</p>
    <div class="h-teal" style="margin-top:18px">Strategy for online Learning</div>
    <p class="lorem">Lorem ipsum dolor sit amet, consectetur adipiscing elit, sed do eiusmod tempor incididunt ut labore et dolore magna aliqua.</p>
  </div>
  <div class="pg">PAGE | 11</div>
</section>

<!-- 12 tower list pink -->
<section class="slide">
  <div class="abs photo-tower" style="left:0;top:0;width:198px;height:100%" role="img" aria-label="Photo looking up at a glass office tower"></div>
  <p class="abs" style="left:35px;top:65px;width:130px;text-align:center;color:#fff;font-size:7.5px;line-height:1.3">Lorem ipsum dolor sit amet, consectetur adipiscing elit, sed do eiusmod tempor incididunt ut labore et dolore magna aliqua. Lorem ipsum dolor sit amet, consectetur adipiscing elit, sed do eiusmod tempor incididunt ut labore et dolore magna aliqua.</p>
  <p class="abs" style="left:222px;top:48px;width:155px;color:var(--teal);font-size:4.6px;line-height:1.45;font-weight:700">Lorem ipsum dolor sit amet, consectetur adipiscing elit, sed do eiusmod tempor incididunt ut labore et dolore magna aliqua. Lorem ipsum dolor sit amet, consectetur adipiscing elit.</p>
  <div class="abs" style="left:227px;top:98px;width:150px;display:grid;gap:7px">
    <div class="row"><span class="dot"></span><p class="lorem">Lorem ipsum dolor sit amet, consectetur adipiscing elit, sed do eiusmod tempor incididunt.</p></div>
    <div class="row"><span class="dot"></span><p class="lorem">Lorem ipsum dolor sit amet, consectetur adipiscing elit, sed do eiusmod tempor incididunt.</p></div>
    <div class="row"><span class="dot"></span><p class="lorem">Lorem ipsum dolor sit amet, consectetur adipiscing elit, sed do eiusmod tempor incididunt.</p></div>
    <div class="row"><span class="dot"></span><p class="lorem">Lorem ipsum dolor sit amet, consectetur adipiscing elit, sed do eiusmod tempor incididunt.</p></div>
  </div>
  <div class="logo foot"><i></i>BT</div>
  <div class="pg">PAGE | 12</div>
</section>

<!-- 13 tower list teal -->
<section class="slide">
  <div class="abs photo-tower" style="left:0;top:0;width:198px;height:100%" role="img" aria-label="Photo looking up at a glass office tower"></div>
  <p class="abs" style="left:35px;top:65px;width:130px;text-align:center;color:#fff;font-size:7.5px;line-height:1.3">Lorem ipsum dolor sit amet, consectetur adipiscing elit, sed do eiusmod tempor incididunt ut labore et dolore magna aliqua. Lorem ipsum dolor sit amet, consectetur adipiscing elit, sed do eiusmod tempor incididunt ut labore et dolore magna aliqua.</p>
  <p class="abs" style="left:222px;top:48px;width:155px;color:var(--teal);font-size:4.6px;line-height:1.45;font-weight:700">Lorem ipsum dolor sit amet, consectetur adipiscing elit, sed do eiusmod tempor incididunt ut labore et dolore magna aliqua. Lorem ipsum dolor sit amet, consectetur adipiscing elit.</p>
  <div class="abs" style="left:227px;top:98px;width:150px;display:grid;gap:7px">
    <div class="row"><span class="dot" style="border-color:var(--teal)"></span><p class="lorem">Lorem ipsum dolor sit amet, consectetur adipiscing elit, sed do eiusmod tempor incididunt.</p></div>
    <div class="row"><span class="dot" style="border-color:var(--teal)"></span><p class="lorem">Lorem ipsum dolor sit amet, consectetur adipiscing elit, sed do eiusmod tempor incididunt.</p></div>
    <div class="row"><span class="dot" style="border-color:var(--teal)"></span><p class="lorem">Lorem ipsum dolor sit amet, consectetur adipiscing elit, sed do eiusmod tempor incididunt.</p></div>
    <div class="row"><span class="dot" style="border-color:var(--teal)"></span><p class="lorem">Lorem ipsum dolor sit amet, consectetur adipiscing elit, sed do eiusmod tempor incididunt.</p></div>
  </div>
  <div class="logo foot"><i></i>BT</div>
  <div class="pg">PAGE | 13</div>
</section>

<!-- 14 three columns -->
<section class="slide">
  <div class="accent"></div>
  <div class="abs" style="left:44px;top:65px;width:320px;display:grid;grid-template-columns:repeat(3,1fr);gap:18px">
    <div><h3 class="h-sm">Add Awesome<br>Title Here</h3><p class="lorem" style="margin-top:10px">Lorem ipsum dolor sit amet, consectetur adipiscing elit, sed do eiusmod tempor incididunt ut labore et dolore magna aliqua.</p><p class="lorem" style="margin-top:6px">Lorem ipsum dolor sit amet, consectetur adipiscing elit, sed. Lorem ipsum dolor sit amet, consectetur adipiscing elit, sed.</p><div style="height:2px;background:var(--pink);margin-top:12px"></div></div>
    <div><h3 class="h-sm">Add Awesome<br>Title Here</h3><p class="lorem" style="margin-top:10px">Lorem ipsum dolor sit amet, consectetur adipiscing elit, sed do eiusmod tempor incididunt ut labore et dolore magna aliqua.</p><p class="lorem" style="margin-top:6px">Lorem ipsum dolor sit amet, consectetur adipiscing elit, sed. Lorem ipsum dolor sit amet, consectetur adipiscing elit, sed.</p><div style="height:2px;background:var(--pink);margin-top:12px"></div></div>
    <div><h3 class="h-sm">Add Awesome<br>Title Here</h3><p class="lorem" style="margin-top:10px">Lorem ipsum dolor sit amet, consectetur adipiscing elit, sed do eiusmod tempor incididunt ut labore et dolore magna aliqua.</p><p class="lorem" style="margin-top:6px">Lorem ipsum dolor sit amet, consectetur adipiscing elit, sed. Lorem ipsum dolor sit amet, consectetur adipiscing elit, sed.</p><div style="height:2px;background:var(--pink);margin-top:12px"></div></div>
  </div>
  <div class="logo foot"><i></i>BT</div>
  <div class="pg">PAGE | 14</div>
</section>

<!-- 15 project grid -->
<section class="slide">
  <div class="accent"></div>
  <div class="abs" style="left:38px;top:70px;width:330px;display:grid;grid-template-columns:1fr 1fr;gap:12px 40px">
    <div class="row"><span class="icon-c"></span><div><div class="h-sm" style="font-size:5px">Project name</div><p class="lorem">Lorem ipsum dolor sit amet, nec an dictas equidem appellantur, ut has commune accommodare.</p></div></div>
    <div class="row"><span class="icon-c"></span><div><div class="h-sm" style="font-size:5px">Project name</div><p class="lorem">Lorem ipsum dolor sit amet, nec an dictas equidem appellantur, ut has commune accommodare.</p></div></div>
    <div class="row"><span class="icon-c"></span><div><div class="h-sm" style="font-size:5px">Project name</div><p class="lorem">Lorem ipsum dolor sit amet, nec an dictas equidem appellantur, ut has commune accommodare.</p></div></div>
    <div class="row"><span class="icon-c"></span><div><div class="h-sm" style="font-size:5px">Project name</div><p class="lorem">Lorem ipsum dolor sit amet, nec an dictas equidem appellantur, ut has commune accommodare.</p></div></div>
    <div class="row"><span class="icon-c"></span><div><div class="h-sm" style="font-size:5px">Project name</div><p class="lorem">Lorem ipsum dolor sit amet, nec an dictas equidem appellantur, ut has commune accommodare.</p></div></div>
    <div class="row"><span class="icon-c"></span><div><div class="h-sm" style="font-size:5px">Project name</div><p class="lorem">Lorem ipsum dolor sit amet, nec an dictas equidem appellantur, ut has commune accommodare.</p></div></div>
  </div>
  <div class="logo foot"><i></i>BT</div>
  <div class="pg">PAGE | 15</div>
</section>

<!-- 16 numbered grid -->
<section class="slide">
  <div class="accent"></div>
  <div class="abs" style="left:26px;top:70px;width:340px;display:grid;grid-template-columns:repeat(3,1fr);gap:18px 10px">
    <div class="row"><span class="num">01</span><div><div class="h-sm" style="font-size:4.8px">Your Text Here</div><p class="lorem">Lorem ipsum dolor sit amet.</p></div></div>
    <div class="row"><span class="num">02</span><div><div class="h-sm" style="font-size:4.8px">Your Text Here</div><p class="lorem">Lorem ipsum dolor sit amet.</p></div></div>
    <div class="row"><span class="num">03</span><div><div class="h-sm" style="font-size:4.8px">Your Text Here</div><p class="lorem">Lorem ipsum dolor sit amet.</p></div></div>
    <div class="row"><span class="num">04</span><div><div class="h-sm" style="font-size:4.8px">Your Text Here</div><p class="lorem">Lorem ipsum dolor sit amet.</p></div></div>
    <div class="row"><span class="num">05</span><div><div class="h-sm" style="font-size:4.8px">Your Text Here</div><p class="lorem">Lorem ipsum dolor sit amet.</p></div></div>
    <div class="row"><span class="num">06</span><div><div class="h-sm" style="font-size:4.8px">Your Text Here</div><p class="lorem">Lorem ipsum dolor sit amet.</p></div></div>
    <div class="row"><span class="num">07</span><div><div class="h-sm" style="font-size:4.8px">Your Text Here</div><p class="lorem">Lorem ipsum dolor sit amet.</p></div></div>
    <div class="row"><span class="num">08</span><div><div class="h-sm" style="font-size:4.8px">Your Text Here</div><p class="lorem">Lorem ipsum dolor sit amet.</p></div></div>
    <div class="row"><span class="num">09</span><div><div class="h-sm" style="font-size:4.8px">Your Text Here</div><p class="lorem">Lorem ipsum dolor sit amet.</p></div></div>
    <div class="row"><span class="num">10</span><div><div class="h-sm" style="font-size:4.8px">Your Text Here</div><p class="lorem">Lorem ipsum dolor sit amet.</p></div></div>
    <div class="row"><span class="num">11</span><div><div class="h-sm" style="font-size:4.8px">Your Text Here</div><p class="lorem">Lorem ipsum dolor sit amet.</p></div></div>
    <div class="row"><span class="num">12</span><div><div class="h-sm" style="font-size:4.8px">Your Text Here</div><p class="lorem">Lorem ipsum dolor sit amet.</p></div></div>
  </div>
  <div class="logo foot"><i></i>BT</div>
  <div class="pg">PAGE | 16</div>
</section>

<!-- 17 three photo cards -->
<section class="slide">
  <div class="abs" style="left:0;top:0;width:100%;height:122px;background:var(--silver)"></div>
  <h2 class="abs" style="left:22px;top:32px;color:#fff;font-size:13px;font-weight:400;line-height:1.25">Your awesome<br>text here</h2>
  <div class="abs" style="left:22px;top:68px;color:#fff;font-size:4px;letter-spacing:1.6px">SUB TITLE GOES HERE</div>
  <p class="lorem white abs" style="left:190px;top:30px;width:185px">Lorem ipsum dolor sit amet, consectetur adipiscing elit, sed do eiusmod tempor incididunt ut labore et dolore magna aliqua. Lorem ipsum dolor sit amet, consectetur adipiscing elit, sed do eiusmod tempor incididunt ut labore et dolore magna aliqua.</p>
  <div class="abs round photo-compass" style="left:22px;top:90px;width:98px;height:65px" role="img" aria-label="Photo of a hand holding a compass over a landscape"></div>
  <div class="abs round photo-laptop" style="left:150px;top:90px;width:98px;height:65px" role="img" aria-label="Photo of hands typing on a laptop"></div>
  <div class="abs round photo-team" style="left:280px;top:90px;width:98px;height:65px" role="img" aria-label="Photo of a team meeting around a table"></div>
  <div class="abs" style="left:22px;top:163px;width:98px"><div class="h-sm" style="font-size:5px;font-weight:400">Your Text Here</div><p class="lorem">Lorem ipsum dolor sit amet, consectetur adipiscing elit, sed do eiusmod tempor incididunt ut labore et dolore magna aliqua.</p></div>
  <div class="abs" style="left:150px;top:163px;width:98px"><div class="h-sm" style="font-size:5px;font-weight:400">Your Text Here</div><p class="lorem">Lorem ipsum dolor sit amet, consectetur adipiscing elit, sed do eiusmod tempor incididunt ut labore et dolore magna aliqua.</p></div>
  <div class="abs" style="left:280px;top:163px;width:98px"><div class="h-sm" style="font-size:5px;font-weight:400">Your Text Here</div><p class="lorem">Lorem ipsum dolor sit amet, consectetur adipiscing elit, sed do eiusmod tempor incididunt ut labore et dolore magna aliqua.</p></div>
  <div class="logo foot"><i></i>BT</div>
  <div class="pg">PAGE | 17</div>
</section>

<!-- 18 city photo box -->
<section class="slide">
  <div class="abs photo-city" style="left:60px;top:0;right:0;height:205px;border-radius:0 0 0 60px" role="img" aria-label="Photo of a busy city street at sunset"></div>
  <div class="abs" style="left:0;top:110px;width:198px;height:88px;background:var(--teal);padding:8px 22px">
    <h2 style="color:#fff;font-size:14px;font-weight:400">Your Text Here</h2>
    <p class="lorem white" style="margin-top:6px">Lorem Ipsum the printing and typesetting industry. Lorem Ipsum has been the industry's standard dummy text ever since the 1500s, when an unknown printer took a galley of type and scrambled it to make a type specimen book.</p>
  </div>
  <div class="logo foot"><i></i>BT</div>
  <div class="pg">PAGE | 18</div>
</section>

<!-- 19 blank -->
<section class="slide">
  <div class="accent"></div>
  <div class="logo foot"><i></i>BT</div>
  <div class="pg">PAGE | 19</div>
</section>

<!-- 20 text photo percent -->
<section class="slide">
  <h2 class="abs" style="left:28px;top:36px;font-size:12px;font-weight:400;line-height:1.1">Add your awesome<br>text here</h2>
  <div class="abs" style="left:20px;top:70px;width:330px;height:125px;background:var(--paper);border-radius:6px"></div>
  <p class="lorem abs" style="left:33px;top:86px;width:165px;text-align:justify">There are many variations of passages of Lorem Ipsum available, but the majority have suffered alteration in some form, by injected humour, or randomised words which don't look even slightly believable. If you are going to use a passage of Lorem Ipsum, you need to be sure there isn't anything embarrassing hidden in the middle of text. All the Lorem Ipsum generators on the Internet tend to repeat predefined chunks as necessary.</p>
  <div class="abs round photo-lightbox" style="left:205px;top:22px;width:175px;height:112px" role="img" aria-label="Photo of a lightbox sign reading think outside the box"></div>
  <div class="abs" style="left:213px;top:118px;width:74px;height:74px;border-radius:50%;background:var(--teal);border:4px solid #fff;color:#fff;text-align:center;padding-top:15px">
    <div style="font-size:16px;font-weight:300">50%</div><p class="lorem white" style="width:44px;margin:2px auto 0">Lorem ipsum dolor sit amet.</p>
  </div>
  <div class="logo foot"><i></i>BT</div>
  <div class="pg">PAGE | 20</div>
</section>

<!-- 21 cards photo -->
<section class="slide">
  <h2 class="abs" style="left:25px;top:25px;font-size:12px;font-weight:400;line-height:1.15">Add your Awesome<br>Text Here</h2>
  <p class="lorem abs" style="left:25px;top:62px;width:185px">Lorem Ipsum the printing and typesetting industry. Lorem Ipsum has been the industry's standard dummy text ever since the 1500s, when an unknown printer took a galley of type and scrambled it to make a type specimen book.</p>
  <div class="abs photo-notes round" style="left:238px;top:12px;width:146px;height:198px" role="img" aria-label="Photo of a hand placing sticky notes on a wall"></div>
  <div class="abs round" style="left:22px;top:112px;width:80px;height:82px;background:var(--teal);padding:18px 6px;text-align:center"><div class="h-sm" style="font-size:4.8px;color:#fff">Project name</div><p class="lorem white">Lorem ipsum dolor sit amet, nec an dictas equidem appellantur.</p></div>
  <div class="abs round card-sh" style="left:106px;top:112px;width:80px;height:82px;padding:18px 6px;text-align:center"><div class="h-sm" style="font-size:4.8px">Project name</div><p class="lorem">Lorem ipsum dolor sit amet, nec an dictas equidem appellantur.</p></div>
  <div class="abs round card-sh" style="left:190px;top:112px;width:80px;height:82px;padding:18px 6px;text-align:center"><div class="h-sm" style="font-size:4.8px">Project name</div><p class="lorem">Lorem ipsum dolor sit amet, nec an dictas equidem appellantur.</p></div>
  <div class="logo foot"><i></i>BT</div>
  <div class="pg">PAGE | 21</div>
</section>

<!-- 22 three bands -->
<section class="slide">
  <h2 class="abs" style="left:20px;top:48px;font-size:12px;font-weight:400;line-height:1.15">Lorem ipsum dolor sit<br>amet elit et dolor</h2>
  <p class="lorem abs" style="left:20px;top:86px;width:140px">Lorem ipsum dolor sit amet, consectetur adipiscing elit, sed do eiusmod tempor incididunt ut labore et dolore magna aliqua.</p>
  <div class="abs photo-meeting" style="left:175px;top:18px;width:210px;height:128px" role="img" aria-label="Black and white photo of two people meeting by a window"></div>
  <div class="abs" style="left:0;top:145px;width:135px;height:77px;background:var(--teal);padding:24px 14px"><div class="h-sm" style="font-size:5px;color:#fff">Lorem ipsum dolor</div><p class="lorem white">Lorem ipsum dolor sit amet, consectetur adipiscing elit, sed do eiusmod tempor.</p></div>
  <div class="abs" style="left:135px;top:145px;width:130px;height:77px;background:var(--pink);padding:24px 14px"><div class="h-sm" style="font-size:5px;color:#fff">Lorem ipsum dolor</div><p class="lorem white">Lorem ipsum dolor sit amet, consectetur adipiscing elit, sed do eiusmod tempor.</p></div>
  <div class="abs" style="left:265px;top:145px;width:130px;height:77px;background:var(--silver);padding:24px 14px"><div class="h-sm" style="font-size:5px;color:#fff">Lorem ipsum dolor</div><p class="lorem white">Lorem ipsum dolor sit amet, consectetur adipiscing elit, sed do eiusmod tempor.</p></div>
  <div class="abs" style="left:28px;top:132px;width:22px;height:22px;border-radius:50%;background:var(--teal);border:2px solid #fff"></div>
  <div class="abs" style="left:152px;top:132px;width:22px;height:22px;border-radius:50%;background:var(--pink);border:2px solid #fff"></div>
  <div class="abs" style="left:290px;top:132px;width:22px;height:22px;border-radius:50%;background:var(--silver);border:2px solid #fff"></div>
  <div class="logo foot"><i></i>BT</div>
  <div class="pg">PAGE | 22</div>
</section>

<!-- 23 cycle diagram -->
<section class="slide">
  <div class="accent"></div>
  <svg class="fill" viewBox="0 0 395 222">
    <g fill="none" stroke-width="22">
      <path d="M200 58 A57 57 0 0 1 249 86" stroke="#9cd3d1"/>
      <path d="M251 90 A57 57 0 0 1 251 140" stroke="#bfcbce"/>
      <path d="M249 144 A57 57 0 0 1 204 172" stroke="#f6ded1"/>
      <path d="M196 172 A57 57 0 0 1 151 144" stroke="#bfcbce"/>
      <path d="M149 140 A57 57 0 0 1 149 90" stroke="#f6ded1"/>
      <path d="M151 86 A57 57 0 0 1 196 58" stroke="#bfcbce"/>
    </g>
    <circle cx="200" cy="115" r="38" fill="#fff"/>
  </svg>
  <div class="abs" style="left:170px;top:110px;width:60px;text-align:center;font-size:7px;font-weight:700">Brennig-Tautz</div>
  <div class="abs" style="left:40px;top:42px;width:95px;text-align:right"><div class="h-sm" style="font-size:4.8px">Lorem ipsum dolor</div><p class="lorem">Lorem ipsum dolor sit amet, consectetur adipiscing elit, sed do eiusmod tempor</p></div>
  <div class="abs" style="left:25px;top:98px;width:95px;text-align:right"><div class="h-sm" style="font-size:4.8px">Lorem ipsum dolor</div><p class="lorem">Lorem ipsum dolor sit amet, consectetur adipiscing elit, sed do eiusmod tempor</p></div>
  <div class="abs" style="left:40px;top:157px;width:95px;text-align:right"><div class="h-sm" style="font-size:4.8px">Lorem ipsum dolor</div><p class="lorem">Lorem ipsum dolor sit amet, consectetur adipiscing elit, sed do eiusmod tempor</p></div>
  <div class="abs" style="left:262px;top:42px;width:95px"><div class="h-sm" style="font-size:4.8px">Lorem ipsum dolor</div><p class="lorem">Lorem ipsum dolor sit amet, consectetur adipiscing elit, sed do eiusmod tempor</p></div>
  <div class="abs" style="left:278px;top:98px;width:95px"><div class="h-sm" style="font-size:4.8px">Lorem ipsum dolor</div><p class="lorem">Lorem ipsum dolor sit amet, consectetur adipiscing elit, sed do eiusmod tempor</p></div>
  <div class="abs" style="left:262px;top:157px;width:95px"><div class="h-sm" style="font-size:4.8px">Lorem ipsum dolor</div><p class="lorem">Lorem ipsum dolor sit amet, consectetur adipiscing elit, sed do eiusmod tempor</p></div>
  <div class="logo foot"><i></i>BT</div>
  <div class="pg">PAGE | 23</div>
</section>

<!-- 24 timeline -->
<section class="slide">
  <div class="accent"></div>
  <svg class="fill" viewBox="0 0 395 222">
    <line x1="55" y1="122" x2="345" y2="122" stroke="#bfcbce" stroke-width="1"/>
    <g stroke="#fff" stroke-width="2">
      <circle cx="55" cy="122" r="12" fill="#9cd3d1"/><circle cx="128" cy="122" r="12" fill="#f6ded1"/><circle cx="200" cy="122" r="12" fill="#9cd3d1"/><circle cx="272" cy="122" r="12" fill="#f6ded1"/><circle cx="345" cy="122" r="12" fill="#9cd3d1"/>
    </g>
    <g stroke="#bfcbce" stroke-width=".6"><line x1="55" y1="92" x2="55" y2="108"/><line x1="200" y1="92" x2="200" y2="108"/><line x1="345" y1="92" x2="345" y2="108"/><line x1="128" y1="136" x2="128" y2="150"/><line x1="272" y1="136" x2="272" y2="150"/></g>
  </svg>
  <div class="abs" style="left:15px;top:62px;width:80px;text-align:center"><div class="h-sm" style="font-size:4.8px">Content Title here</div><p class="lorem">Lorem ipsum dolor sit amet, nec an dictas equidem appellantur.</p></div>
  <div class="abs" style="left:160px;top:62px;width:80px;text-align:center"><div class="h-sm" style="font-size:4.8px">Content Title here</div><p class="lorem">Lorem ipsum dolor sit amet, nec an dictas equidem appellantur.</p></div>
  <div class="abs" style="left:305px;top:62px;width:80px;text-align:center"><div class="h-sm" style="font-size:4.8px">Content Title here</div><p class="lorem">Lorem ipsum dolor sit amet, nec an dictas equidem appellantur.</p></div>
  <div class="abs" style="left:88px;top:155px;width:80px;text-align:center"><div class="h-sm" style="font-size:4.8px">Content Title here</div><p class="lorem">Lorem ipsum dolor sit amet, nec an dictas equidem.</p></div>
  <div class="abs" style="left:232px;top:155px;width:80px;text-align:center"><div class="h-sm" style="font-size:4.8px">Content Title here</div><p class="lorem">Lorem ipsum dolor sit amet, nec an dictas equidem.</p></div>
  <div class="logo foot"><i></i>BT</div>
  <div class="pg">PAGE | 24</div>
</section>

<!-- 25 table -->
<section class="slide">
  <div class="accent"></div>
  <table class="tbl" style="top:68px">
    <tr><th>ADD YOUR TITLE</th><th>ADD YOUR TITLE</th><th>ADD YOUR TITLE</th><th>ADD YOUR TITLE</th></tr>
    <tr><td><b>Project name</b>Lorem Ipsum is simply dummy text, a galley of type and scrambled.</td><td><b>Project name</b>Lorem Ipsum is simply dummy text, a galley of type and scrambled.</td><td><b>Project name</b>Lorem Ipsum is simply dummy text, a galley of type and scrambled.</td><td><b>Project name</b>Lorem Ipsum is simply dummy text, a galley of type and scrambled.</td></tr>
    <tr><td><b>Project name</b>Lorem Ipsum is simply dummy text, a galley of type and scrambled.</td><td><b>Project name</b>Lorem Ipsum is simply dummy text, a galley of type and scrambled.</td><td><b>Project name</b>Lorem Ipsum is simply dummy text, a galley of type and scrambled.</td><td><b>Project name</b>Lorem Ipsum is simply dummy text, a galley of type and scrambled.</td></tr>
  </table>
  <div class="logo foot"><i></i>BT</div>
  <div class="pg">PAGE | 25</div>
</section>

<!-- 26 money circles -->
<section class="slide">
  <div class="accent"></div>
  <svg class="fill" viewBox="0 0 395 222">
    <g stroke-width="4">
      <circle cx="78" cy="92" r="38" fill="#9cd3d1" stroke="#e6f3f2"/>
      <circle cx="203" cy="92" r="38" fill="#f6ded1" stroke="#fbf0ea"/>
      <circle cx="330" cy="92" r="38" fill="#bfcbce" stroke="#e9eef0"/>
    </g>
    <g fill="#fff" font-family="Lato, sans-serif" font-size="19" text-anchor="middle" font-weight="300">
      <text x="78" y="92">$1M</text><text x="203" y="92">$10M</text><text x="330" y="92">$15M</text>
    </g>
    <g stroke="#bfcbce" stroke-width=".5"><line x1="78" y1="132" x2="78" y2="185"/><line x1="203" y1="132" x2="203" y2="185"/><line x1="330" y1="132" x2="330" y2="185"/></g>
  </svg>
  <div class="abs" style="left:40px;top:150px;width:76px;text-align:center;background:#fff"><div class="h-sm" style="font-size:4.8px">Lorem ipsum dolor</div><p class="lorem">Lorem ipsum dolor sit amet, consectetur adipiscing elit, sed do eiusmod tempor</p></div>
  <div class="abs" style="left:165px;top:150px;width:76px;text-align:center;background:#fff"><div class="h-sm" style="font-size:4.8px">Lorem ipsum dolor</div><p class="lorem">Lorem ipsum dolor sit amet, consectetur adipiscing elit, sed do eiusmod tempor</p></div>
  <div class="abs" style="left:292px;top:150px;width:76px;text-align:center;background:#fff"><div class="h-sm" style="font-size:4.8px">Lorem ipsum dolor</div><p class="lorem">Lorem ipsum dolor sit amet, consectetur adipiscing elit, sed do eiusmod tempor</p></div>
  <div class="logo foot"><i></i>BT</div>
  <div class="pg">PAGE | 26</div>
</section>

<!-- 27 percent rings -->
<section class="slide">
  <h2 class="abs" style="left:0;width:100%;top:40px;text-align:center;font-size:16px;font-weight:400">Your awesome text here</h2>
  <p class="lorem abs" style="left:85px;top:66px;width:225px;text-align:center">Lorem Ipsum the printing and typesetting industry. Lorem Ipsum has been the industry's standard dummy text ever since the 1500s, when an unknown printer took a galley of type and scrambled it to make a type specimen book.</p>
  <svg class="fill" viewBox="0 0 395 222">
    <g fill="none" stroke-width="3">
      <circle cx="112" cy="140" r="27" stroke="#eeeeee"/><circle cx="198" cy="140" r="27" stroke="#eeeeee"/><circle cx="283" cy="140" r="27" stroke="#eeeeee"/>
      <circle cx="112" cy="140" r="27" stroke="#f6ded1" stroke-dasharray="85 170" transform="rotate(-90 112 140)"/>
      <circle cx="198" cy="140" r="27" stroke="#9cd3d1" stroke-dasharray="127 170" transform="rotate(-90 198 140)"/>
      <circle cx="283" cy="140" r="27" stroke="#bfcbce" stroke-dasharray="68 170" transform="rotate(-90 283 140)"/>
    </g>
    <g fill="#666666" font-family="Lato, sans-serif" font-size="13" text-anchor="middle"><text x="112" y="145">50%</text><text x="198" y="145">75%</text><text x="283" y="145">40%</text></g>
  </svg>
  <p class="lorem abs" style="left:85px;top:180px;width:55px;text-align:center">Lorem ipsum dolor amet consectetur dolor</p>
  <p class="lorem abs" style="left:170px;top:180px;width:55px;text-align:center">Lorem ipsum dolor amet consectetur dolor</p>
  <p class="lorem abs" style="left:256px;top:180px;width:55px;text-align:center">Lorem ipsum dolor amet consectetur dolor</p>
  <div class="logo foot"><i></i>BT</div>
  <div class="pg">PAGE | 27</div>
</section>

<!-- 28 company statistics -->
<section class="slide">
  <svg class="fill" viewBox="0 0 395 222" font-family="Lato, sans-serif">
    <g stroke="#eeeeee" stroke-width=".5"><line x1="40" y1="40" x2="200" y2="40"/><line x1="40" y1="75" x2="200" y2="75"/><line x1="40" y1="110" x2="200" y2="110"/><line x1="40" y1="145" x2="200" y2="145"/></g>
    <line x1="40" y1="180" x2="200" y2="180" stroke="#bfcbce" stroke-width=".6"/>
    <g fill="#9cd3d1"><rect x="50" y="92" width="6" height="88"/><rect x="87" y="131" width="6" height="49"/><rect x="124" y="96" width="6" height="84"/><rect x="161" y="145" width="6" height="35"/></g>
    <g fill="#f6ded1"><rect x="57" y="131" width="6" height="49"/><rect x="94" y="131" width="6" height="49"/><rect x="131" y="160" width="6" height="20"/><rect x="168" y="131" width="6" height="49"/></g>
    <g fill="#bfcbce"><rect x="64" y="145" width="6" height="35"/><rect x="101" y="92" width="6" height="88"/><rect x="138" y="160" width="6" height="20"/><rect x="175" y="110" width="6" height="70"/></g>
    <g fill="#807f84" font-size="4" text-anchor="end"><text x="35" y="42">5</text><text x="35" y="77">4</text><text x="35" y="112">3</text><text x="35" y="147">2</text><text x="35" y="182">0</text></g>
    <g fill="#807f84" font-size="4" text-anchor="middle"><text x="60" y="190">Category 1</text><text x="97" y="190">Category 2</text><text x="134" y="190">Category 3</text><text x="171" y="190">Category 4</text></g>
  </svg>
  <div class="abs" style="left:250px;top:42px;font-size:4.6px;letter-spacing:1.5px;color:var(--gray)">LOREM IPSUM DOLOR</div>
  <h2 class="abs" style="left:250px;top:52px;font-size:15px;font-weight:400;line-height:1.15">Company<br>Statistics</h2>
  <div class="abs row" style="left:250px;top:112px"><span class="icon-c" style="width:14px;height:14px;background:none;border:1px solid var(--pink)"></span><div><div style="font-size:5px">Description here</div><p class="lorem">Our mission is delivering<br>creative solution through visual</p></div></div>
  <div class="abs row" style="left:250px;top:142px"><span class="icon-c" style="width:14px;height:14px;background:none;border:1px solid var(--teal)"></span><div><div style="font-size:5px">Description here</div><p class="lorem">Our mission is delivering<br>creative solution through visual</p></div></div>
  <div class="logo foot"><i></i>BT</div>
  <div class="pg">PAGE | 28</div>
</section>

<!-- 29 bar values -->
<section class="slide">
  <div class="accent"></div>
  <svg class="fill" viewBox="0 0 395 222" font-family="Lato, sans-serif">
    <line x1="30" y1="180" x2="180" y2="180" stroke="#bfcbce" stroke-width=".6"/>
    <rect x="40" y="86" width="12" height="94" fill="#9cd3d1"/><rect x="75" y="139" width="12" height="41" fill="#f6ded1"/><rect x="110" y="115" width="12" height="65" fill="#bfcbce"/><rect x="145" y="168" width="12" height="12" fill="#807f84"/>
    <g fill="#bfcbce"><rect x="39" y="72" width="14" height="9" rx="1"/><rect x="74" y="125" width="14" height="9" rx="1"/><rect x="109" y="101" width="14" height="9" rx="1"/><rect x="144" y="154" width="14" height="9" rx="1"/></g>
    <g fill="#fff" font-size="5" text-anchor="middle"><text x="46" y="78.5">80</text><text x="81" y="131.5">35</text><text x="116" y="107.5">55</text><text x="151" y="160.5">10</text></g>
    <g fill="#807f84" font-size="4" text-anchor="middle"><text x="46" y="190">Category 1</text><text x="81" y="190">Category 2</text><text x="116" y="190">Category 3</text><text x="151" y="190">Category 4</text></g>
  </svg>
  <div class="abs" style="left:210px;top:98px;width:165px;display:grid;gap:8px">
    <div class="row"><span class="dot" style="background:var(--pink);border:0"></span><p class="lorem" style="color:var(--dim)">Lorem ipsum dolor sit amet, quam id eros. Vestibulum luctus velit. Pretium ante, integer a blandit. Nullam nunc nisi, rutrum rhoncus.</p></div>
    <div class="row"><span class="dot" style="background:var(--pink);border:0"></span><p class="lorem" style="color:var(--dim)">Imperdiet in pulvinar. Tellus augue. Elit urna dignissim. Est inceptos. Ligula augue, elit amet, et vestibulum.</p></div>
    <div class="row"><span class="dot" style="background:var(--pink);border:0"></span><p class="lorem" style="color:var(--dim)">Dolor lacus gravida. Elit placerat risus, cursus orci, eget blandit. Et maecenas, lorem mollis. Vestibulum feugiat pulvinar, tortor donec massa.</p></div>
  </div>
  <div class="logo foot"><i></i>BT</div>
  <div class="pg">PAGE | 29</div>
</section>

<!-- 30 line chart -->
<section class="slide">
  <svg class="fill" viewBox="0 0 395 222" font-family="Lato, sans-serif">
    <line x1="22" y1="168" x2="200" y2="168" stroke="#bfcbce" stroke-width=".5"/>
    <path d="M25 130 C35 100 42 100 48 120 S58 160 66 140 S78 60 88 90 S100 150 110 130 S122 75 132 110 S145 150 155 100 S168 60 178 105 S190 150 196 125" fill="none" stroke="#f6ded1" stroke-width="1.6"/>
    <path d="M25 140 C35 120 42 150 50 120 S62 80 72 125 S82 160 92 135 S104 100 116 140 S130 165 140 120 S152 95 162 130 S176 150 186 120 S194 120 198 130" fill="none" stroke="#9cd3d1" stroke-width="1.6"/>
    <g fill="#807f84" font-size="4"><text x="36" y="116">4.4</text><text x="82" y="82">5.7</text><text x="22" y="150">2.4</text><text x="74" y="160">1.8</text><text x="106" y="154">2.8</text><text x="128" y="142">3.2</text><text x="150" y="150">2.4</text><text x="172" y="88">6.7</text><text x="182" y="116">5.8</text></g>
    <g fill="#807f84" font-size="3.6"><text x="22" y="178">2005</text><text x="36" y="178">2006</text><text x="50" y="178">2007</text><text x="64" y="178">2008</text><text x="78" y="178">2009</text><text x="92" y="178">2010</text><text x="106" y="178">2011</text><text x="120" y="178">2012</text><text x="134" y="178">2013</text><text x="148" y="178">2014</text><text x="162" y="178">2015</text><text x="176" y="178">2016</text></g>
  </svg>
  <h2 class="abs" style="left:232px;top:78px;font-size:15px;font-weight:400">Chart</h2>
  <div class="abs" style="left:232px;top:96px;font-size:6px;color:var(--gray)">Lorem ipsum dolor sit amet</div>
  <div class="abs" style="left:232px;top:112px;width:140px;display:grid;gap:6px">
    <div class="row"><span class="dot" style="width:3px;height:3px;background:var(--teal);border:0;margin-top:1px"></span><p class="lorem">Lorem ipsum dolor sit amet, consectetur adipiscing elit, sed do eiusmod tempor incididunt ut labore et dolore magna aliqua.</p></div>
    <div class="row"><span class="dot" style="width:3px;height:3px;background:var(--teal);border:0;margin-top:1px"></span><p class="lorem">Lorem ipsum dolor sit amet, consectetur adipiscing elit. Lorem ipsum dolor sit amet, consectetur adipiscing elit, sed do eiusmod tempor.</p></div>
  </div>
  <div class="pg">PAGE | 30</div>
</section>

<!-- 31 serpentine timeline -->
<section class="slide">
  <svg class="fill" viewBox="0 0 395 222" font-family="Lato, sans-serif">
    <path d="M22 28 L22 40 Q22 66 50 66 L350 66 Q378 66 378 100 Q378 134 350 134 L50 134 Q22 134 22 168 Q22 200 50 200 L395 200" fill="none" stroke="#e2e6e7" stroke-width="1.2"/>
    <line x1="22" y1="20" x2="22" y2="36" stroke="#f6ded1" stroke-width="1.2"/>
    <g fill="#f6ded1"><circle cx="85" cy="66" r="3"/><circle cx="272" cy="66" r="3"/><circle cx="178" cy="134" r="3"/></g>
    <g fill="#9cd3d1"><circle cx="178" cy="66" r="3"/><circle cx="85" cy="134" r="3"/><circle cx="272" cy="134" r="3"/></g>
    <g><rect x="85" y="71" width="40" height="6" rx="3" fill="#f6ded1"/><rect x="178" y="71" width="40" height="6" rx="3" fill="#9cd3d1"/><rect x="272" y="71" width="40" height="6" rx="3" fill="#f6ded1"/>
    <rect x="85" y="139" width="40" height="6" rx="3" fill="#9cd3d1"/><rect x="178" y="139" width="40" height="6" rx="3" fill="#f6ded1"/><rect x="272" y="139" width="40" height="6" rx="3" fill="#9cd3d1"/></g>
    <g fill="#fff" font-size="4.4" font-weight="700"><text x="89" y="75.6">2012</text><text x="182" y="75.6">2014</text><text x="276" y="75.6">2016</text><text x="89" y="143.6">2018</text><text x="182" y="143.6">2019</text><text x="276" y="143.6">2020</text></g>
  </svg>
  <p class="lorem abs" style="left:85px;top:81px;width:60px;color:var(--dim)">Lorem Ipsum is simply dummy unknown printer took a galley of type.</p>
  <p class="lorem abs" style="left:178px;top:81px;width:60px;color:var(--dim)">Lorem Ipsum is simply dummy unknown printer took a galley of type.</p>
  <p class="lorem abs" style="left:272px;top:81px;width:60px;color:var(--dim)">Lorem Ipsum is simply dummy unknown printer took a galley of type.</p>
  <p class="lorem abs" style="left:85px;top:149px;width:60px;color:var(--dim)">Lorem Ipsum is simply dummy unknown printer took a galley of type.</p>
  <p class="lorem abs" style="left:178px;top:149px;width:60px;color:var(--dim)">Lorem Ipsum is simply dummy unknown printer took a galley of type.</p>
  <p class="lorem abs" style="left:272px;top:149px;width:60px;color:var(--dim)">Lorem Ipsum is simply dummy unknown printer took a galley of type.</p>
  <div class="logo foot"><i></i>BT</div>
  <div class="pg">PAGE | 31</div>
</section>

<!-- 32 thank you card -->
<section class="slide">
  <div class="abs card-sh" style="left:45px;top:16px;width:110px;height:196px">
    <div class="logo" style="left:8px;top:18px;font-size:9px"><i></i>Brennig-Tautz</div>
    <div class="abs contact-row" style="left:0;top:56px;width:100%;background:var(--teal);color:#fff;padding-left:10px;height:22px">
      <svg width="8" height="8" viewBox="0 0 10 10"><circle cx="5" cy="5" r="4" fill="none" stroke="#fff"/><path d="M1 5h8M5 1q3 4 0 8q-3-4 0-8" fill="none" stroke="#fff" stroke-width=".7"/></svg>www.brennig-tautz.de</div>
    <div class="abs contact-row" style="left:10px;top:84px;color:var(--dim);height:26px;border-bottom:.5px solid #eee;width:90px">
      <svg width="7" height="9" viewBox="0 0 8 10"><path d="M4 10 C1 6 0 5 0 4 A4 4 0 0 1 8 4 C8 5 7 6 4 10Z" fill="#9cd3d1"/></svg><span>Here to write your<br>Company adress</span></div>
    <div class="abs contact-row" style="left:10px;top:114px;color:var(--dim);border-bottom:.5px solid #eee;width:90px;height:24px">
      <svg width="8" height="8" viewBox="0 0 10 10"><path d="M2 0 L4 3 L3 4 Q4 6 6 7 L7 6 L10 8 L8 10 Q2 9 0 2Z" fill="#9cd3d1"/></svg>(555) 014-2290</div>
    <div class="abs contact-row" style="left:10px;top:144px;color:var(--dim);border-bottom:.5px solid #eee;width:90px;height:24px">
      <svg width="9" height="7" viewBox="0 0 10 7"><rect width="10" height="7" fill="#9cd3d1"/><path d="M0 0 L5 4 L10 0" fill="none" stroke="#fff" stroke-width=".8"/></svg>info@brennig-tautz.de</div>
    <div class="abs" style="left:38px;top:176px;display:flex;gap:4px"><span style="width:8px;height:8px;background:var(--dim)"></span><span style="width:8px;height:8px;background:var(--dim)"></span></div>
  </div>
  <h2 class="abs" style="left:218px;top:96px;font-size:22px;font-weight:400;color:#222">Thank You!</h2>
</section>

<!-- 33 thank you teal -->
<section class="slide" style="background:var(--teal)">
  <div class="abs photo-office" style="left:215px;top:0;width:200px;height:100%;border-radius:80px 0 0 0" role="img" aria-label="Overhead photo of a desk with laptops and coffee"></div>
  <h2 class="abs" style="left:25px;top:28px;font-size:15px;font-weight:700;color:#fff">Thank You!</h2>
  <div class="abs" style="left:25px;top:60px;color:#fff;display:grid">
    <div class="contact-row"><svg width="8" height="8" viewBox="0 0 10 10"><circle cx="5" cy="5" r="4" fill="none" stroke="#fff"/><path d="M1 5h8M5 1q3 4 0 8q-3-4 0-8" fill="none" stroke="#fff" stroke-width=".7"/></svg>www.brennig-tautz.de</div>
    <div class="contact-row"><svg width="7" height="9" viewBox="0 0 8 10"><path d="M4 10 C1 6 0 5 0 4 A4 4 0 0 1 8 4 C8 5 7 6 4 10Z" fill="#fff"/></svg>Here to write your Company adress</div>
    <div class="contact-row"><svg width="8" height="8" viewBox="0 0 10 10"><path d="M2 0 L4 3 L3 4 Q4 6 6 7 L7 6 L10 8 L8 10 Q2 9 0 2Z" fill="#fff"/></svg>(555) 014-2290</div>
    <div class="contact-row"><svg width="9" height="7" viewBox="0 0 10 7"><rect width="10" height="7" fill="#fff"/><path d="M0 0 L5 4 L10 0" fill="none" stroke="#9cd3d1" stroke-width=".8"/></svg>info@brennig-tautz.de</div>
  </div>
  <div class="logo light" style="left:25px;top:192px;font-size:11px"><i></i>Brennig-Tautz</div>
</section>

</main>
</body>
</html>
```